A Hair, Beauty and Nails Wholesalers Needs a Business Card Design

We need a business card design for our company which is being passed from parents to daughter, so we wont to re-launch the company with an updated, modern, sophisticated, elegant, chic and fresh look which still incorporates the original colour scheme of Hot Pink, Dark Grey and White. The original logo which is attached can be used on the card but we would like to see some designs with the logo and some without, as we have not yet decided if we want the logo on the card. The name of our company is 'Velmora Supplies' and the name of our website is VelmoraGlowandPolish.example.au. We specialise in supplying a massive range of Hair, Beauty and Nail products to the industry. We are based in QLD, Australia but ship many orders via our website all across Australia.

```html
<!DOCTYPE html>
<html lang="en">
<head>
<meta charset="utf-8">
<title>Velmora Supplies – Business Card</title>
<link rel="stylesheet" href="https://fonts.googleapis.com/css2?family=Open+Sans:wght@400;600&display=swap">
<style>
  :root {
    --hot-pink: #e6195f;
    --pink-soft: #f0508a;
    --card-light: #f7f7f7;
    --card-edge: #d4d4d4;
    --grey-text: #6b6b6b;
    --grey-dark: #4a4a4a;
    --grey-icon: #8c8c8c;
  }
  html, body {
    margin: 0;
    padding: 0;
    overflow: hidden;
    background: #ffffff;
  }
  .card {
    position: relative;
    width: 1200px;
    height: 725px;
    overflow: hidden;
    font-family: "Open Sans", Arial, sans-serif;
    background: radial-gradient(ellipse at 62% 45%, var(--card-light) 0%, #ececec 55%, var(--card-edge) 100%);
  }
  .tool-wave {
    position: absolute;
    left: 0;
    top: 0;
    width: 500px;
    height: 640px;
  }
  .brand-name {
    position: absolute;
    left: 600px;
    top: 96px;
    width: 560px;
    margin: 0;
    font-size: 66px;
    font-weight: 600;
    line-height: 1;
    color: var(--grey-dark);
    text-align: center;
    white-space: nowrap;
  }
  .contact-list {
    position: absolute;
    left: 540px;
    top: 320px;
    width: 650px;
    margin: 0;
    padding: 0;
    list-style: none;
  }
  .contact-item {
    display: flex;
    align-items: center;
    height: 36px;
    margin-bottom: 32px;
    font-size: 32px;
    line-height: 36px;
    color: var(--grey-text);
    white-space: nowrap;
  }
  .contact-item.web-line {
    font-size: 27px;
    letter-spacing: -0.3px;
  }
  .contact-item.address {
    align-items: flex-start;
    height: auto;
    color: var(--grey-dark);
    line-height: 48px;
    margin-top: -4px;
  }
  .contact-icon {
    width: 48px;
    height: 36px;
    margin-right: 52px;
    flex: none;
  }
  .contact-icon svg {
    display: block;
    margin: 0 auto;
  }
  .contact-item.address .contact-icon {
    height: 48px;
  }
</style>
</head>
<body>
  <div class="card">
    <svg class="tool-wave" viewBox="0 0 500 640" role="img" aria-label="Flowing pink wave made of hair, beauty and nail tool silhouettes">
      <defs>
        <linearGradient id="waveFill" x1="0" y1="0" x2="1" y2="1">
          <stop offset="0" stop-color="var(--hot-pink)"/>
          <stop offset="1" stop-color="var(--pink-soft)"/>
        </linearGradient>
      </defs>
      <path d="M0,95 C90,60 170,55 250,95 C330,135 380,170 440,195 L470,300 L492,440 L478,600 C420,545 330,540 220,580 C140,605 60,620 0,612 Z" fill="url(#waveFill)"/>
    </svg>

    <h1 class="brand-name">Velmora Supplies</h1>

    <ul class="contact-list">
      <li class="contact-item">
        <span class="contact-icon">
          <svg width="40" height="36" viewBox="0 0 40 36"><circle cx="20" cy="11" r="8" fill="var(--grey-icon)"/><path d="M4,36 C4,24 12,20 20,20 C28,20 36,24 36,36 Z" fill="var(--grey-icon)"/></svg>
        </span>
        Marisa Delacourt
      </li>
      <li class="contact-item">
        <span class="contact-icon">
          <svg width="20" height="36" viewBox="0 0 20 36"><path d="M6,10 C3,14 3,22 7,26 L10,24 L8,20 C7,18 7,16 8,14 L10,12 Z" fill="var(--grey-icon)"/></svg>
        </span>
        (07) 5550 0199
      </li>
      <li class="contact-item web-line">
        <span class="contact-icon">
          <svg width="24" height="36" viewBox="0 0 24 36"><rect x="2" y="12" width="20" height="13" fill="none" stroke="var(--grey-icon)" stroke-width="2"/><path d="M2,12 L12,20 L22,12" fill="none" stroke="var(--grey-icon)" stroke-width="2"/></svg>
        </span>
        admin@velmoraglowandpolish.example.au
      </li>
      <li class="contact-item web-line">
        <span class="contact-icon">
          <svg width="24" height="36" viewBox="0 0 24 36"><circle cx="12" cy="18" r="9" fill="none" stroke="var(--grey-icon)" stroke-width="2"/><path d="M3,18 H21 M12,9 C8,13 8,23 12,27 M12,9 C16,13 16,23 12,27" fill="none" stroke="var(--grey-icon)" stroke-width="1.5"/></svg>
        </span>
        www.VelmoraGlowandPolish.example.au
      </li>
      <li class="contact-item address">
        <span class="contact-icon">
          <svg width="24" height="48" viewBox="0 0 24 48"><path d="M2,25 L12,16 L22,25" fill="none" stroke="var(--grey-icon)" stroke-width="2"/><rect x="5" y="24" width="14" height="10" fill="none" stroke="var(--grey-icon)" stroke-width="2"/><rect x="10" y="28" width="4" height="6" fill="var(--grey-icon)"/></svg>
        </span>
        <span>27 Kestrel Lane<br>TOOWOOMBA, QLD, 4350</span>
      </li>
    </ul>
  </div>
</body>
</html>
```